One page financial canvas needed

I am in the process of developing a financial planning process that uses a one page canvas as a tool for financial education and to explain simple and complex financial strategies to clients. I have the layout and content sorted, just need a hand making it look professional.

It should be a fairly simple project and i have attached a very rough hand drawn canvas showing the desired layout and content. Please feel free to be creative with the design keeping in mind this layout has been chosen to achieve certain outcomes.

Target Market(s)

25-45 Year old Homeowners who are interested in taking better care of the finances

Industry/Entity Type

Financial

Colors

Designer to choose colors to be used in the design.

Requirements
Must have
• very close to the layout in the attached file

```html
<!DOCTYPE html>
<html lang="en">
<head>
<meta charset="utf-8">
<title>Financial Planning Canvas</title>
<link rel="stylesheet" href="https://fonts.googleapis.com/css2?family=Montserrat:wght@500&family=Roboto+Condensed:wght@800&display=swap">
<style>
:root{
  --goals-bg:#b9eaf0;
  --money-bg:#d3e8d1;
  --people-bg:#dadff2;
  --goals-ink:#2a7d9c;
  --money-ink:#2e8f70;
  --people-ink:#5e2d84;
  --goals-bar:#2d7fa0;
  --money-bar:#2f9270;
  --people-bar:#7b3d9f;
  --footer-bg:#d8d8d8;
  --white:#ffffff;
  --divider:#e4e4e4;
}
*{margin:0;padding:0;box-sizing:border-box}
html,body{width:1200px;height:834px;overflow:hidden;background:var(--white)}
.canvas{position:relative;width:1200px;height:834px;font-family:"Montserrat",Arial,sans-serif}
.column{position:absolute;top:0;height:742px}
.column--goals{left:0;width:302px;background:var(--goals-bg)}
.column--money{left:302px;width:598px;background:var(--money-bg)}
.column--people{left:900px;width:300px;background:var(--people-bg)}
.rule{position:absolute;top:742px;height:10px}
.rule--goals{left:0;width:302px;background:var(--goals-bar)}
.rule--money{left:302px;width:598px;background:var(--money-bar)}
.rule--people{left:900px;width:300px;background:var(--people-bar)}
.footer{position:absolute;top:752px;left:0;width:1200px;height:82px;background:var(--footer-bg)}
.flow{position:absolute;left:0;top:0;width:1200px;height:742px}
.label{position:absolute;height:47px;background:var(--white);display:flex;align-items:center;font-size:16px;letter-spacing:.3px}
.label::after{content:"";position:absolute;top:47px;border-left:10px solid transparent;border-right:10px solid transparent;border-top:10px solid var(--white)}
.label__icon{width:59px;height:100%;display:flex;align-items:center;justify-content:center}
.label__text{flex:1;padding:0 14px}
.label--icon-left .label__icon{border-right:2px solid var(--divider)}
.label--icon-right .label__icon{border-left:2px solid var(--divider)}
.label--icon-right .label__text{text-align:right}
.label--goals{left:9px;top:9px;width:282px;color:var(--goals-ink)}
.label--goals::after{left:16px}
.label--money{color:var(--money-ink);width:218px}
.label--income{left:316px;top:14px}
.label--income::after{left:18px}
.label--expenses{left:668px;top:14px}
.label--expenses::after{right:18px}
.label--assets{left:316px;top:368px}
.label--assets::after{left:18px}
.label--debt{left:668px;top:368px}
.label--debt::after{right:18px}
.label--people{left:911px;width:269px;color:var(--people-ink)}
.label--people .label__text{text-align:left}
.label--people::after{left:16px}
.label--fears{top:10px}
.label--frustrations{top:262px}
.label--partners{top:505px}
.label--time{left:12px;top:772px;width:1178px;height:47px;color:var(--people-ink);font-size:15px}
.label--time::after{display:none}
.label--time .label__icon{width:52px}
.hub-text{font-family:"Roboto Condensed","Arial Narrow",sans-serif;font-weight:800;fill:var(--white);text-anchor:middle}
</style>
</head>
<body>
<main class="canvas">
  <section class="column column--goals"></section>
  <section class="column column--money"></section>
  <section class="column column--people"></section>
  <div class="rule rule--goals"></div>
  <div class="rule rule--money"></div>
  <div class="rule rule--people"></div>
  <div class="footer"></div>

  <svg class="flow" viewBox="0 0 1200 742" aria-hidden="true">
    <line x1="534" y1="37" x2="668" y2="37" stroke="#fff" stroke-width="7"/>
    <line x1="534" y1="391" x2="668" y2="391" stroke="#fff" stroke-width="7"/>
    <line x1="600" y1="37" x2="600" y2="670" stroke="#fff" stroke-width="7"/>
    <circle cx="600" cy="37" r="16" fill="var(--money-bg)" stroke="#fff" stroke-width="5"/>
    <circle cx="600" cy="391" r="54" fill="var(--money-bar)" stroke="#fff" stroke-width="6"/>
    <text class="hub-text" x="600" y="390" font-size="24">CASH</text>
    <text class="hub-text" x="600" y="413" font-size="24">FLOW</text>
    <path d="M518 737 A82 82 0 0 1 682 737 Z" fill="var(--money-bar)" stroke="#fff" stroke-width="5"/>
    <text class="hub-text" x="600" y="718" font-size="20">WEALTH</text>
  </svg>

  <div class="label label--goals label--icon-right">
    <span class="label__text">GOALS</span>
    <span class="label__icon">
      <svg width="36" height="36" viewBox="0 0 36 36"><circle cx="16" cy="20" r="13" fill="none" stroke="var(--goals-ink)" stroke-width="4"/><circle cx="16" cy="20" r="6" fill="none" stroke="var(--goals-ink)" stroke-width="3"/><circle cx="16" cy="20" r="2" fill="var(--goals-ink)"/><path d="M17 19 L31 6" stroke="var(--goals-ink)" stroke-width="3"/><path d="M27 3 L34 2 L33 9 Z" fill="var(--goals-ink)"/></svg>
    </span>
  </div>

  <div class="label label--money label--income label--icon-left">
    <span class="label__icon">
      <svg width="34" height="30" viewBox="0 0 34 30"><ellipse cx="17" cy="17" rx="13" ry="10" fill="var(--money-ink)"/><rect x="9" y="23" width="4" height="6" fill="var(--money-ink)"/><rect x="21" y="23" width="4" height="6" fill="var(--money-ink)"/><rect x="29" y="14" width="4" height="5" fill="var(--money-ink)"/><circle cx="17" cy="5" r="4" fill="var(--money-ink)"/></svg>
    </span>
    <span class="label__text">INCOME</span>
  </div>

  <div class="label label--money label--expenses label--icon-right">
    <span class="label__text">EXPENSESS</span>
    <span class="label__icon">
      <svg width="38" height="30" viewBox="0 0 38 30"><rect x="6" y="2" width="30" height="18" rx="2" fill="none" stroke="var(--money-ink)" stroke-width="3" transform="rotate(8 21 11)"/><rect x="2" y="9" width="30" height="18" rx="2" fill="var(--money-ink)"/><circle cx="17" cy="18" r="5" fill="#fff"/></svg>
    </span>
  </div>

  <div class="label label--money label--assets label--icon-left">
    <span class="label__icon">
      <svg width="28" height="34" viewBox="0 0 28 34"><path d="M9 2 H19 L16 9 H12 Z" fill="var(--money-ink)"/><path d="M11 10 H17 C27 15 28 32 14 32 C0 32 1 15 11 10 Z" fill="var(--money-ink)"/><text x="14" y="27" font-size="12" font-family="Arial,sans-serif" font-weight="700" fill="#fff" text-anchor="middle">$</text></svg>
    </span>
    <span class="label__text">ASSETS</span>
  </div>

  <div class="label label--money label--debt label--icon-right">
    <span class="label__text">DEBT</span>
    <span class="label__icon">
      <svg width="36" height="30" viewBox="0 0 36 30"><rect x="8" y="3" width="26" height="17" rx="2" fill="var(--money-ink)" transform="rotate(-10 21 11)"/><rect x="2" y="10" width="26" height="17" rx="2" fill="#fff" stroke="var(--money-ink)" stroke-width="3"/><rect x="2" y="14" width="26" height="3" fill="var(--money-ink)"/><rect x="6" y="21" width="8" height="2" fill="var(--money-ink)"/></svg>
    </span>
  </div>

  <div class="label label--people label--fears label--icon-right">
    <span class="label__text">FEARS</span>
    <span class="label__icon">
      <svg width="30" height="34" viewBox="0 0 30 34"><path d="M14 2 C24 2 28 9 27 16 L29 21 L26 22 L26 27 L20 28 L20 33 L7 33 L7 25 C2 21 1 15 3 10 C5 5 9 2 14 2 Z" fill="var(--people-ink)"/><text x="15" y="21" font-size="15" font-family="Arial,sans-serif" font-weight="700" fill="#fff" text-anchor="middle">?</text></svg>
    </span>
  </div>

  <div class="label label--people label--frustrations label--icon-right">
    <span class="label__text">FRUSTRATIONS</span>
    <span class="label__icon">
      <svg width="28" height="34" viewBox="0 0 28 34"><circle cx="12" cy="6" r="5" fill="var(--people-ink)"/><path d="M8 13 C13 11 18 15 18 21 L24 30 L20 32 L14 24 L8 32 L4 30 L9 22 C6 20 5 16 8 13 Z" fill="var(--people-ink)"/></svg>
    </span>
  </div>

  <div class="label label--people label--partners label--icon-right">
    <span class="label__text">PARTNERS</span>
    <span class="label__icon">
      <svg width="36" height="34" viewBox="0 0 36 34"><circle cx="7" cy="7" r="4" fill="var(--people-ink)"/><circle cx="29" cy="7" r="4" fill="var(--people-ink)"/><circle cx="18" cy="5" r="4.5" fill="var(--people-ink)"/><rect x="2" y="12" width="10" height="20" rx="2" fill="var(--people-ink)"/><rect x="24" y="12" width="10" height="20" rx="2" fill="var(--people-ink)"/><rect x="12" y="11" width="12" height="22" rx="2" fill="var(--people-ink)" stroke="#fff" stroke-width="1.5"/></svg>
    </span>
  </div>

  <div class="label label--time label--icon-left">
    <span class="label__icon">
      <svg width="30" height="32" viewBox="0 0 30 32"><rect x="11" y="1" width="8" height="3" fill="var(--people-ink)"/><rect x="13.5" y="3" width="3" height="4" fill="var(--people-ink)"/><circle cx="15" cy="19" r="11" fill="none" stroke="var(--people-ink)" stroke-width="3.5"/><path d="M15 12 V19 L20 22" fill="none" stroke="var(--people-ink)" stroke-width="2.5"/></svg>
    </span>
    <span class="label__text">TIME</span>
  </div>
</main>
</body>
</html>
```